Flavour Wheel - Illustrator Graph

I need my basic layout, from the sample I provided, turned into a professional looking flavour wheel.

I have attached a sample of a final design I like, but please use your own creativity also.

All the exact words I need are on the uploaded illustration.

I would need the file supplied to me in .ai

Industry/Entity Type

Wheel

Font styles to use
Sans Serif

Colors

Designer to choose colors to be used in the design.

Requirements
Must have
• Files must be supplied in .ai format with fonts not outlined.
• I need each segment separated so I can change the colours if needed myself.
Nice to have
• I like small white gaps between the sections.

```html
<!DOCTYPE html>
<html lang="en">
<head>
<meta charset="utf-8">
<title>Flavour Wheel</title>
<link rel="stylesheet" href="https://fonts.googleapis.com/css2?family=Source+Sans+3:wght@400;600&display=swap">
<style>
  :root {
    --paper: #fdfdfd;
    --gap: #ffffff;

    --sour: #2199a4; --sour-bitter: #4ab3c3; --sour-vinegary: #79c5d2; --sour-citrus: #90cfdb; --sour-ink: #1a9bb0;
    --earthy: #a67b52; --earthy-floral: #c4a286; --earthy-herby: #bb9470; --earthy-nutty: #b48a61; --earthy-ink: #a67843;
    --sweet: #9e1c62; --sweet-buttery: #c97aa3; --sweet-fruity: #bc5f93; --sweet-sugary: #b0497f; --sweet-caramel: #a2386f; --sweet-ink: #a01c62;
    --salty: #5f9a80; --salty-charred: #84b09b; --salty-briney: #72a68e; --salty-ink: #5f9a80;
    --savoury: #d7a22a; --savoury-meatiness: #dcaf48; --savoury-umami: #e4c06f; --savoury-ink: #d9a42a;
    --spicy: #a52530; --spicy-chilli: #b53d48; --spicy-peppery: #c3636c; --spicy-cajun: #d68e96; --spicy-ink: #a8202f;
    --smokey: #7f8a8f; --smokey-woody: #909ca2; --smokey-fruity: #a7b1b5; --smokey-acrid: #b6bec1; --smokey-ink: #7f8a8f;
  }
  html, body { margin: 0; padding: 0; overflow: hidden; background: var(--paper); }
  .canvas { width: 1200px; height: 1200px; background: var(--paper); overflow: hidden; }
  .wheel { display: block; font-family: "Source Sans 3", sans-serif; text-transform: uppercase; }
  .segment { fill: none; }
  .segment--core { stroke-width: 215; }
  .segment--outer { stroke-width: 125; }
  .divider { stroke: var(--gap); stroke-width: 6; }
  .core-label { fill: #fff; font-size: 30px; letter-spacing: 0.5px; }
  .sub-label { fill: #fff; font-size: 18px; letter-spacing: 0.3px; }
  .ingredient rect { fill: var(--tone); }
  .ingredient text { fill: var(--tone); font-size: 19px; letter-spacing: 0.2px; }
  .tone-sour { --tone: var(--sour-ink); }
  .tone-earthy { --tone: var(--earthy-ink); }
  .tone-sweet { --tone: var(--sweet-ink); }
  .tone-salty { --tone: var(--salty-ink); }
  .tone-savoury { --tone: var(--savoury-ink); }
  .tone-spicy { --tone: var(--spicy-ink); }
  .tone-smokey { --tone: var(--smokey-ink); }
  .out { text-anchor: start; }
  .in { text-anchor: end; }
</style>
</head>
<body>
<div class="canvas">
<svg class="wheel" width="1200" height="1200" viewBox="0 0 1500 1500" role="img" aria-label="Flavour wheel">
 <g transform="translate(752 768)">

  <!-- core flavours -->
  <g class="ring ring--core">
   <circle class="segment segment--core" r="232.5" pathLength="360" stroke="var(--sour)" stroke-dasharray="54 360" transform="rotate(-117)"/>
   <circle class="segment segment--core" r="232.5" pathLength="360" stroke="var(--earthy)" stroke-dasharray="62 360" transform="rotate(-63)"/>
   <circle class="segment segment--core" r="232.5" pathLength="360" stroke="var(--sweet)" stroke-dasharray="55 360" transform="rotate(-1)"/>
   <circle class="segment segment--core" r="232.5" pathLength="360" stroke="var(--salty)" stroke-dasharray="36 360" transform="rotate(54)"/>
   <circle class="segment segment--core" r="232.5" pathLength="360" stroke="var(--savoury)" stroke-dasharray="41 360" transform="rotate(90)"/>
   <circle class="segment segment--core" r="232.5" pathLength="360" stroke="var(--spicy)" stroke-dasharray="57 360" transform="rotate(131)"/>
   <circle class="segment segment--core" r="232.5" pathLength="360" stroke="var(--smokey)" stroke-dasharray="55 360" transform="rotate(188)"/>
  </g>

  <!-- sub flavours -->
  <g class="ring ring--outer">
   <circle class="segment segment--outer" r="407.5" pathLength="360" stroke="var(--sour-bitter)" stroke-dasharray="18 360" transform="rotate(-117)"/>
   <circle class="segment segment--outer" r="407.5" pathLength="360" stroke="var(--sour-vinegary)" stroke-dasharray="18 360" transform="rotate(-99)"/>
   <circle class="segment segment--outer" r="407.5" pathLength="360" stroke="var(--sour-citrus)" stroke-dasharray="18 360" transform="rotate(-81)"/>
   <circle class="segment segment--outer" r="407.5" pathLength="360" stroke="var(--earthy-floral)" stroke-dasharray="21 360" transform="rotate(-63)"/>
   <circle class="segment segment--outer" r="407.5" pathLength="360" stroke="var(--earthy-herby)" stroke-dasharray="20 360" transform="rotate(-42)"/>
   <circle class="segment segment--outer" r="407.5" pathLength="360" stroke="var(--earthy-nutty)" stroke-dasharray="21 360" transform="rotate(-22)"/>
   <circle class="segment segment--outer" r="407.5" pathLength="360" stroke="var(--sweet-buttery)" stroke-dasharray="14 360" transform="rotate(-1)"/>
   <circle class="segment segment--outer" r="407.5" pathLength="360" stroke="var(--sweet-fruity)" stroke-dasharray="12 360" transform="rotate(13)"/>
   <circle class="segment segment--outer" r="407.5" pathLength="360" stroke="var(--sweet-sugary)" stroke-dasharray="14 360" transform="rotate(25)"/>
   <circle class="segment segment--outer" r="407.5" pathLength="360" stroke="var(--sweet-caramel)" stroke-dasharray="15 360" transform="rotate(39)"/>
   <circle class="segment segment--outer" r="407.5" pathLength="360" stroke="var(--salty-charred)" stroke-dasharray="18 360" transform="rotate(54)"/>
   <circle class="segment segment--outer" r="407.5" pathLength="360" stroke="var(--salty-briney)" stroke-dasharray="18 360" transform="rotate(72)"/>
   <circle class="segment segment--outer" r="407.5" pathLength="360" stroke="var(--savoury-meatiness)" stroke-dasharray="20 360" transform="rotate(90)"/>
   <circle class="segment segment--outer" r="407.5" pathLength="360" stroke="var(--savoury-umami)" stroke-dasharray="21 360" transform="rotate(110)"/>
   <circle class="segment segment--outer" r="407.5" pathLength="360" stroke="var(--spicy-chilli)" stroke-dasharray="17 360" transform="rotate(131)"/>
   <circle class="segment segment--outer" r="407.5" pathLength="360" stroke="var(--spicy-peppery)" stroke-dasharray="20 360" transform="rotate(148)"/>
   <circle class="segment segment--outer" r="407.5" pathLength="360" stroke="var(--spicy-cajun)" stroke-dasharray="20 360" transform="rotate(168)"/>
   <circle class="segment segment--outer" r="407.5" pathLength="360" stroke="var(--smokey-woody)" stroke-dasharray="18 360" transform="rotate(188)"/>
   <circle class="segment segment--outer" r="407.5" pathLength="360" stroke="var(--smokey-fruity)" stroke-dasharray="18 360" transform="rotate(206)"/>
   <circle class="segment segment--outer" r="407.5" pathLength="360" stroke="var(--smokey-acrid)" stroke-dasharray="19 360" transform="rotate(224)"/>
  </g>

  <!-- white gaps -->
  <g class="dividers">
   <line class="divider" x1="0" y1="-118" x2="0" y2="-476" transform="rotate(-27)"/>
   <line class="divider" x1="0" y1="-118" x2="0" y2="-476" transform="rotate(27)"/>
   <line class="divider" x1="0" y1="-118" x2="0" y2="-476" transform="rotate(89)"/>
   <line class="divider" x1="0" y1="-118" x2="0" y2="-476" transform="rotate(144)"/>
   <line class="divider" x1="0" y1="-118" x2="0" y2="-476" transform="rotate(180)"/>
   <line class="divider" x1="0" y1="-118" x2="0" y2="-476" transform="rotate(221)"/>
   <line class="divider" x1="0" y1="-118" x2="0" y2="-476" transform="rotate(278)"/>
   <line class="divider" x1="0" y1="-338" x2="0" y2="-476" transform="rotate(-9)"/>
   <line class="divider" x1="0" y1="-338" x2="0" y2="-476" transform="rotate(9)"/>
   <line class="divider" x1="0" y1="-338" x2="0" y2="-476" transform="rotate(48)"/>
   <line class="divider" x1="0" y1="-338" x2="0" y2="-476" transform="rotate(68)"/>
   <line class="divider" x1="0" y1="-338" x2="0" y2="-476" transform="rotate(103)"/>
   <line class="divider" x1="0" y1="-338" x2="0" y2="-476" transform="rotate(115)"/>
   <line class="divider" x1="0" y1="-338" x2="0" y2="-476" transform="rotate(129)"/>
   <line class="divider" x1="0" y1="-338" x2="0" y2="-476" transform="rotate(162)"/>
   <line class="divider" x1="0" y1="-338" x2="0" y2="-476" transform="rotate(200)"/>
   <line class="divider" x1="0" y1="-338" x2="0" y2="-476" transform="rotate(238)"/>
   <line class="divider" x1="0" y1="-338" x2="0" y2="-476" transform="rotate(258)"/>
   <line class="divider" x1="0" y1="-338" x2="0" y2="-476" transform="rotate(296)"/>
   <line class="divider" x1="0" y1="-338" x2="0" y2="-476" transform="rotate(314)"/>
   <circle r="342.5" fill="none" stroke="var(--gap)" stroke-width="5"/>
  </g>

  <!-- core labels -->
  <g class="core-labels" text-anchor="middle">
   <text class="core-label" dy="0.35em" transform="rotate(0) translate(0 -205) rotate(90)">Sour</text>
   <text class="core-label" dy="0.35em" transform="rotate(58) translate(0 -205) rotate(-90)">Earthy</text>
   <text class="core-label" dy="0.35em" transform="rotate(116.5) translate(0 -205) rotate(-90)">Sweet</text>
   <text class="core-label" dy="0.35em" transform="rotate(162) translate(0 -205) rotate(118)">Salty</text>
   <text class="core-label" dy="0.35em" transform="rotate(200.5) translate(0 -205) rotate(90)">Savoury</text>
   <text class="core-label" dy="0.35em" transform="rotate(249.5) translate(0 -205) rotate(90)">Spicy</text>
   <text class="core-label" dy="0.35em" transform="rotate(305.5) translate(0 -205) rotate(90)">Smokey</text>
  </g>

  <!-- sub labels -->
  <g class="sub-labels" text-anchor="middle">
   <text class="sub-label" dy="0.35em" transform="rotate(-18) translate(0 -407) rotate(90)">Bitter</text>
   <text class="sub-label" dy="0.35em" transform="rotate(0) translate(0 -407) rotate(90)">Vinegary</text>
   <text class="sub-label" dy="0.35em" transform="rotate(18) translate(0 -407) rotate(-90)">Citrus</text>
   <text class="sub-label" dy="0.35em" transform="rotate(37.5) translate(0 -407) rotate(-90)">Floral</text>
   <text class="sub-label" dy="0.35em" transform="rotate(58) translate(0 -407) rotate(-90)">Herby</text>
   <text class="sub-label" dy="0.35em" transform="rotate(78.5) translate(0 -407) rotate(-90)">Nutty</text>
   <text class="sub-label" dy="0.35em" transform="rotate(96) translate(0 -407) rotate(-90)">Buttery</text>
   <text class="sub-label" dy="0.35em" transform="rotate(109) translate(0 -407) rotate(-90)">Fruity</text>
   <text class="sub-label" dy="0.35em" transform="rotate(122) translate(0 -407) rotate(-90)">Sugary</text>
   <text class="sub-label" dy="0.35em" transform="rotate(136.5) translate(0 -407) rotate(-90)">Caramel</text>
   <text class="sub-label" dy="0.35em" transform="rotate(153) translate(0 -407) rotate(137)">Charred</text>
   <text class="sub-label" dy="0.35em" transform="rotate(171) translate(0 -407) rotate(109)">Briney</text>
   <text class="sub-label" dy="0.35em" transform="rotate(190) translate(0 -407) rotate(90)">Meatiness</text>
   <text class="sub-label" dy="0.35em" transform="rotate(210.5) translate(0 -407) rotate(90)">Umami</text>
   <text class="sub-label" dy="0.35em" transform="rotate(229.5) translate(0 -407) rotate(90)">Chilli</text>
   <text class="sub-label" dy="0.35em" transform="rotate(248) translate(0 -407) rotate(90)">Peppery</text>
   <text class="sub-label" dy="0.35em" transform="rotate(268) translate(0 -407) rotate(90)">Cajun</text>
   <text class="sub-label" dy="0.35em" transform="rotate(287) translate(0 -407) rotate(90)">Woody</text>
   <text class="sub-label" dy="0.35em" transform="rotate(305) translate(0 -407) rotate(90)">Fruity</text>
   <text class="sub-label" dy="0.35em" transform="rotate(323.5) translate(0 -407) rotate(90)">Acrid</text>
  </g>

  <!-- ingredients: sour -->
  <g class="ingredients tone-sour">
   <g class="ingredient" transform="rotate(-16.6)"><rect x="-12" y="-502" width="24" height="24"/><text class="in" dy="0.35em" transform="translate(0 -512) rotate(90)">Cocktail Bitters</text></g>
   <g class="ingredient" transform="rotate(-13.6)"><rect x="-12" y="-502" width="24" height="24"/><text class="in" dy="0.35em" transform="translate(0 -512) rotate(90)">Citric Acid</text></g>
   <g class="ingredient" transform="rotate(-10.6)"><rect x="-12" y="-502" width="24" height="24"/><text class="in" dy="0.35em" transform="translate(0 -512) rotate(90)">Tamarind</text></g>
   <g class="ingredient" transform="rotate(-1.4)"><rect x="-12" y="-502" width="24" height="24"/><text class="in" dy="0.35em" transform="translate(0 -512) rotate(90)">Rice Vinegar</text></g>
   <g class="ingredient" transform="rotate(1.6)"><rect x="-12" y="-502" width="24" height="24"/><text class="in" dy="0.35em" transform="translate(0 -512) rotate(90)">Balsamic Vinegar</text></g>
   <g class="ingredient" transform="rotate(4.6)"><rect x="-12" y="-502" width="24" height="24"/><text class="in" dy="0.35em" transform="translate(0 -512) rotate(90)">Apple Cider Vinegar</text></g>
   <g class="ingredient" transform="rotate(16.8)"><rect x="-12" y="-502" width="24" height="24"/><text class="out" dy="0.35em" transform="translate(0 -512) rotate(-90)">Sumac</text></g>
   <g class="ingredient" transform="rotate(19.8)"><rect x="-12" y="-502" width="24" height="24"/><text class="out" dy="0.35em" transform="translate(0 -512) rotate(-90)">Zests</text></g>
   <g class="ingredient" transform="rotate(22.8)"><rect x="-12" y="-502" width="24" height="24"/><text class="out" dy="0.35em" transform="translate(0 -512) rotate(-90)">Lime</text></g>
   <g class="ingredient" transform="rotate(25.8)"><rect x="-12" y="-502" width="24" height="24"/><text class="out" dy="0.35em" transform="translate(0 -512) rotate(-90)">Lemon</text></g>
  </g>

  <!-- ingredients: earthy -->
  <g class="ingredients tone-earthy">
   <g class="ingredient" transform="rotate(37.7)"><rect x="-12" y="-502" width="24" height="24"/><text class="out" dy="0.35em" transform="translate(0 -512) rotate(-90)">Coriander</text></g>
   <g class="ingredient" transform="rotate(40.7)"><rect x="-12" y="-502" width="24" height="24"/><text class="out" dy="0.35em" transform="translate(0 -512) rotate(-90)">Celery</text></g>
   <g class="ingredient" transform="rotate(43.8)"><rect x="-12" y="-502" width="24" height="24"/><text class="out" dy="0.35em" transform="translate(0 -512) rotate(-90)">Tea</text></g>
   <g class="ingredient" transform="rotate(46.8)"><rect x="-12" y="-502" width="24" height="24"/><text class="out" dy="0.35em" transform="translate(0 -512) rotate(-90)">Sage</text></g>
   <g class="ingredient" transform="rotate(49.9)"><rect x="-12" y="-502" width="24" height="24"/><text class="out" dy="0.35em" transform="translate(0 -512) rotate(-90)">Oregano</text></g>
   <g class="ingredient" transform="rotate(52.9)"><rect x="-12" y="-502" width="24" height="24"/><text class="out" dy="0.35em" transform="translate(0 -512) rotate(-90)">Thyme</text></g>
   <g class="ingredient" transform="rotate(56)"><rect x="-12" y="-502" width="24" height="24"/><text class="out" dy="0.35em" transform="translate(0 -512) rotate(-90)">Rosemary</text></g>
   <g class="ingredient" transform="rotate(59)"><rect x="-12" y="-502" width="24" height="24"/><text class="out" dy="0.35em" transform="translate(0 -512) rotate(-90)">Bay Leaf</text></g>
   <g class="ingredient" transform="rotate(62.1)"><rect x="-12" y="-502" width="24" height="24"/><text class="out" dy="0.35em" transform="translate(0 -512) rotate(-90)">Fennel</text></g>
   <g class="ingredient" transform="rotate(65.1)"><rect x="-12" y="-502" width="24" height="24"/><text class="out" dy="0.35em" transform="translate(0 -512) rotate(-90)">Five Spice</text></g>
   <g class="ingredient" transform="rotate(68.2)"><rect x="-12" y="-502" width="24" height="24"/><text class="out" dy="0.35em" transform="translate(0 -512) rotate(-90)">Nutmeg</text></g>
   <g class="ingredient" transform="rotate(71.2)"><rect x="-12" y="-502" width="24" height="24"/><text class="out" dy="0.35em" transform="translate(0 -512) rotate(-90)">Tumeric</text></g>
   <g class="ingredient" transform="rotate(74.3)"><rect x="-12" y="-502" width="24" height="24"/><text class="out" dy="0.35em" transform="translate(0 -512) rotate(-90)">Star Anise</text></g>
   <g class="ingredient" transform="rotate(77.3)"><rect x="-12" y="-502" width="24" height="24"/><text class="out" dy="0.35em" transform="translate(0 -512) rotate(-90)">Cinnamon</text></g>
   <g class="ingredient" transform="rotate(80.4)"><rect x="-12" y="-502" width="24" height="24"/><text class="out" dy="0.35em" transform="translate(0 -512) rotate(-90)">Clove</text></g>
   <g class="ingredient" transform="rotate(83.4)"><rect x="-12" y="-502" width="24" height="24"/><text class="out" dy="0.35em" transform="translate(0 -512) rotate(-90)">Pecan</text></g>
   <g class="ingredient" transform="rotate(86.5)"><rect x="-12" y="-502" width="24" height="24"/><text class="out" dy="0.35em" transform="translate(0 -512) rotate(-90)">Coffee</text></g>
  </g>

  <!-- ingredients: sweet -->
  <g class="ingredients tone-sweet">
   <g class="ingredient" transform="rotate(101.6)"><rect x="-12" y="-502" width="24" height="24"/><text class="out" dy="0.35em" transform="translate(0 -512) rotate(-90)">Butter</text></g>
   <g class="ingredient" transform="rotate(107.5)"><rect x="-12" y="-502" width="24" height="24"/><text class="out" dy="0.35em" transform="translate(0 -512) rotate(-90)">Fruit Juice</text></g>
   <g class="ingredient" transform="rotate(110.5)"><rect x="-12" y="-502" width="24" height="24"/><text class="out" dy="0.35em" transform="translate(0 -512) rotate(-90)">Fruits</text></g>
   <g class="ingredient" transform="rotate(113.5)"><rect x="-12" y="-502" width="24" height="24"/><text class="out" dy="0.35em" transform="translate(0 -512) rotate(-90)">Sauce/Ketchup</text></g>
   <g class="ingredient" transform="rotate(122.3)"><rect x="-12" y="-502" width="24" height="24"/><text class="out" dy="0.35em" transform="translate(0 -512) rotate(-90)">Cola</text></g>
   <g class="ingredient" transform="rotate(125.3)"><rect x="-12" y="-502" width="24" height="24"/><text class="out" dy="0.35em" transform="translate(0 -512) rotate(-90)">Agave Nectar</text></g>
   <g class="ingredient" transform="rotate(128.3)"><rect x="-12" y="-502" width="24" height="24"/><text class="out" dy="0.35em" transform="translate(0 -512) rotate(-90)">Sugars</text></g>
   <g class="ingredient" transform="rotate(136.9)"><rect x="-12" y="-502" width="24" height="24"/><text class="out" dy="0.35em" transform="translate(0 -512) rotate(-90)">Honey</text></g>
   <g class="ingredient" transform="rotate(139.9)"><rect x="-12" y="-502" width="24" height="24"/><text class="out" dy="0.35em" transform="translate(0 -512) rotate(-90)">Molasses</text></g>
   <g class="ingredient" transform="rotate(142.9)"><rect x="-12" y="-502" width="24" height="24"/><text class="out" dy="0.35em" transform="translate(0 -512) rotate(-90)">Maple Syrup</text></g>
  </g>

  <!-- ingredients: salty -->
  <g class="ingredients tone-salty">
   <g class="ingredient" transform="rotate(169.6)"><rect x="-12" y="-502" width="24" height="24"/><text class="in" dy="0.35em" transform="translate(0 -512) rotate(90)">Anchovies</text></g>
   <g class="ingredient" transform="rotate(172.6)"><rect x="-12" y="-502" width="24" height="24"/><text class="in" dy="0.35em" transform="translate(0 -512) rotate(90)">Garlic</text></g>
   <g class="ingredient" transform="rotate(175.5)"><rect x="-12" y="-502" width="24" height="24"/><text class="in" dy="0.35em" transform="translate(0 -512) rotate(90)">Sea Salt</text></g>
   <g class="ingredient" transform="rotate(178.4)"><rect x="-12" y="-502" width="24" height="24"/><text class="in" dy="0.35em" transform="translate(0 -512) rotate(90)">Kosher Salt</text></g>
  </g>

  <!-- ingredients: savoury -->
  <g class="ingredients tone-savoury">
   <g class="ingredient" transform="rotate(190.3)"><rect x="-12" y="-502" width="24" height="24"/><text class="in" dy="0.35em" transform="translate(0 -512) rotate(90)">Soy Sauce</text></g>
   <g class="ingredient" transform="rotate(193.3)"><rect x="-12" y="-502" width="24" height="24"/><text class="in" dy="0.35em" transform="translate(0 -512) rotate(90)">Fish Sauce</text></g>
   <g class="ingredient" transform="rotate(196.3)"><rect x="-12" y="-502" width="24" height="24"/><text class="in" dy="0.35em" transform="translate(0 -512) rotate(90)">Worcestershire</text></g>
   <g class="ingredient" transform="rotate(199.3)"><rect x="-12" y="-502" width="24" height="24"/><text class="in" dy="0.35em" transform="translate(0 -512) rotate(90)">Seasoning Sauce</text></g>
   <g class="ingredient" transform="rotate(208)"><rect x="-12" y="-502" width="24" height="24"/><text class="in" dy="0.35em" transform="translate(0 -512) rotate(90)">Phosphates</text></g>
   <g class="ingredient" transform="rotate(211)"><rect x="-12" y="-502" width="24" height="24"/><text class="in" dy="0.35em" transform="translate(0 -512) rotate(90)">Stocks</text></g>
   <g class="ingredient" transform="rotate(214)"><rect x="-12" y="-502" width="24" height="24"/><text class="in" dy="0.35em" transform="translate(0 -512) rotate(90)">Lard</text></g>
   <g class="ingredient" transform="rotate(217)"><rect x="-12" y="-502" width="24" height="24"/><text class="in" dy="0.35em" transform="translate(0 -512) rotate(90)">Yeast Spread</text></g>
   <g class="ingredient" transform="rotate(220)"><rect x="-12" y="-502" width="24" height="24"/><text class="in" dy="0.35em" transform="translate(0 -512) rotate(90)">MSG</text></g>
  </g>

  <!-- ingredients: spicy -->
  <g class="ingredients tone-spicy">
   <g class="ingredient" transform="rotate(238)"><rect x="-12" y="-502" width="24" height="24"/><text class="in" dy="0.35em" transform="translate(0 -512) rotate(90)">Horseradish</text></g>
   <g class="ingredient" transform="rotate(241)"><rect x="-12" y="-502" width="24" height="24"/><text class="in" dy="0.35em" transform="translate(0 -512) rotate(90)">Wasabi</text></g>
   <g class="ingredient" transform="rotate(244)"><rect x="-12" y="-502" width="24" height="24"/><text class="in" dy="0.35em" transform="translate(0 -512) rotate(90)">Pepper</text></g>
   <g class="ingredient" transform="rotate(247)"><rect x="-12" y="-502" width="24" height="24"/><text class="in" dy="0.35em" transform="translate(0 -512) rotate(90)">Cumin</text></g>
   <g class="ingredient" transform="rotate(250)"><rect x="-12" y="-502" width="24" height="24"/><text class="in" dy="0.35em" transform="translate(0 -512) rotate(90)">Allspice</text></g>
   <g class="ingredient" transform="rotate(253)"><rect x="-12" y="-502" width="24" height="24"/><text class="in" dy="0.35em" transform="translate(0 -512) rotate(90)">Szechuan</text></g>
   <g class="ingredient" transform="rotate(256)"><rect x="-12" y="-502" width="24" height="24"/><text class="in" dy="0.35em" transform="translate(0 -512) rotate(90)">Onion</text></g>
   <g class="ingredient" transform="rotate(259)"><rect x="-12" y="-502" width="24" height="24"/><text class="in" dy="0.35em" transform="translate(0 -512) rotate(90)">Chipotle</text></g>
   <g class="ingredient" transform="rotate(262)"><rect x="-12" y="-502" width="24" height="24"/><text class="in" dy="0.35em" transform="translate(0 -512) rotate(90)">Jalapeno</text></g>
   <g class="ingredient" transform="rotate(265)"><rect x="-12" y="-502" width="24" height="24"/><text class="in" dy="0.35em" transform="translate(0 -512) rotate(90)">Hot Sauce</text></g>
   <g class="ingredient" transform="rotate(268)"><rect x="-12" y="-502" width="24" height="24"/><text class="in" dy="0.35em" transform="translate(0 -512) rotate(90)">Habanero</text></g>
   <g class="ingredient" transform="rotate(271)"><rect x="-12" y="-502" width="24" height="24"/><text class="in" dy="0.35em" transform="translate(0 -512) rotate(90)">Red Pepper</text></g>
   <g class="ingredient" transform="rotate(274)"><rect x="-12" y="-502" width="24" height="24"/><text class="in" dy="0.35em" transform="translate(0 -512) rotate(90)">Mustard</text></g>
   <g class="ingredient" transform="rotate(277)"><rect x="-12" y="-502" width="24" height="24"/><text class="in" dy="0.35em" transform="translate(0 -512) rotate(90)">Paprika</text></g>
  </g>

  <!-- ingredients: smokey -->
  <g class="ingredients tone-smokey">
   <g class="ingredient" transform="rotate(288.4)"><rect x="-12" y="-502" width="24" height="24"/><text class="in" dy="0.35em" transform="translate(0 -512) rotate(90)">Hard Woods</text></g>
   <g class="ingredient" transform="rotate(291.4)"><rect x="-12" y="-502" width="24" height="24"/><text class="in" dy="0.35em" transform="translate(0 -512) rotate(90)">Fruit Woods</text></g>
   <g class="ingredient" transform="rotate(294.4)"><rect x="-12" y="-502" width="24" height="24"/><text class="in" dy="0.35em" transform="translate(0 -512) rotate(90)">Charcoal</text></g>
   <g class="ingredient" transform="rotate(309.6)"><rect x="-12" y="-502" width="24" height="24"/><text class="in" dy="0.35em" transform="translate(0 -512) rotate(90)">Whiskey</text></g>
   <g class="ingredient" transform="rotate(312.6)"><rect x="-12" y="-502" width="24" height="24"/><text class="in" dy="0.35em" transform="translate(0 -512) rotate(90)">Bourbon</text></g>
   <g class="ingredient" transform="rotate(331)"><rect x="-12" y="-502" width="24" height="24"/><text class="in" dy="0.35em" transform="translate(0 -512) rotate(90)">Creosote</text></g>
  </g>

 </g>
</svg>
</div>
</body>
</html>
```